Commercial painting company is looking for a creative website designer.

Hi, we just completed our logo project and now ready to launch our website. The project will be done on Squarespace platform. It will contain:
Page 1 HOME
Page 2 SERVICES
Page 3 PICTURES
The content will be written by us. I am not sure bout the pictures, I do not have any to provide. I can buy stock photos if needed.
We are commercial only painting company and have to appeal to commercial, industrial property mangers. We will need CALL, REQUEST FOR ESTIMATE buttons.
If possible to have a live picture on home page would be great. Thank you
Target Market(s)
Property Managers
Industry/Entity Type
Commercial Painting
Other font styles liked:
- Poppins

```html
<!DOCTYPE html>
<html lang="en">
<head>
<meta charset="utf-8">
<title>CoatCraft USA — Commercial Painting</title>
<link rel="stylesheet" href="https://fonts.googleapis.com/css2?family=Poppins:wght@400;500;700;800&display=swap">
<style>
  :root {
    --bg: #262626;
    --footer: #4a2326;
    --red: #c0001c;
    --call: #e3202a;
    --navy: #0c2466;
    --white: #ffffff;
    --text: #f2f2f2;
  }
  * { margin: 0; padding: 0; box-sizing: border-box; }
  html, body { width: 1200px; height: 3504px; overflow: hidden; }
  body { background: var(--bg); font-family: 'Poppins', sans-serif; color: var(--text); position: relative; }
  .abs { position: absolute; }

  .brand { display: flex; align-items: center; gap: 10px; }
  .brand-mark { width: 34px; height: 34px; border-radius: 50%; background: var(--red); flex: none; }
  .brand-name { font-weight: 700; font-size: 20px; color: var(--white); white-space: nowrap; }

  .site-header .brand { left: 146px; top: 64px; }
  .nav { left: 528px; top: 72px; display: flex; gap: 48px; font-size: 14px; font-weight: 500; color: var(--white); }
  .social { display: flex; gap: 26px; }
  .social span { width: 15px; height: 15px; border-radius: 50%; background: var(--white); display: block; }
  .site-header .social { left: 843px; top: 74px; }
  .btn { display: flex; align-items: center; justify-content: center; border-radius: 4px; color: var(--white); font-size: 14px; font-weight: 500; }
  .btn-call { left: 969px; top: 64px; width: 85px; height: 36px; background: var(--call); font-size: 14px; }
  .btn-navy { background: var(--navy); }
  .btn-red { background: var(--red); }

  .hero { left: 144px; top: 162px; width: 912px; height: 550px; overflow: hidden; }
  .hero-photo { position: absolute; inset: 0; background: linear-gradient(160deg, #f3f1ec 0%, #e2ddd3 45%, #d2a14a 70%, #c9c2b6 100%); }
  .hero-band { position: absolute; left: 0; bottom: 0; width: 912px; height: 200px; }
  .hero-title { left: 33px; top: 444px; font-size: 28px; font-weight: 700; line-height: 41px; color: var(--white); }
  .hero .btn { left: 652px; top: 471px; width: 205px; height: 36px; font-size: 14px; }

  .photo { position: absolute; overflow: hidden; }
  .photo-about { left: 144px; top: 853px; width: 445px; height: 646px; background: linear-gradient(180deg, #6d6a66 0%, #5a5754 50%, #9a1020 65%, #8c0d1c 100%); }
  .photo-services { left: 608px; top: 1688px; width: 446px; height: 647px; background: linear-gradient(90deg, #a88f4e 0%, #b21a24 40%, #cfd0d2 62%, #cfd0d2 100%); }
  .photo-services::after, .photo-gallery::after { content: ""; position: absolute; left: 0; right: 0; bottom: 0; height: 36%; background: var(--red); opacity: .9; }
  .photo-gallery { left: 144px; top: 2524px; width: 445px; height: 645px; background: linear-gradient(180deg, #b9bfc6 0%, #e7e7e7 45%, #dcdcdc 100%); }

  h2 { font-size: 44px; font-weight: 700; line-height: 53px; color: var(--white); }
  h2 .accent { color: var(--red); }
  .copy { font-size: 16.5px; line-height: 31.4px; color: var(--text); width: 415px; }

  .about h2 { left: 648px; top: 975px; }
  .about .copy { left: 648px; top: 1110px; }
  .about .btn { left: 648px; top: 1330px; width: 140px; height: 35px; }

  .services h2 { left: 144px; top: 1848px; }
  .services .copy { left: 144px; top: 1914px; }
  .services .btn { left: 144px; top: 2129px; width: 142px; height: 36px; }

  .gallery h2 { left: 648px; top: 2710px; }
  .gallery .copy { left: 648px; top: 2785px; }
  .gallery .btn { left: 648px; top: 2936px; width: 140px; height: 35px; }

  .site-footer { left: 0; top: 3318px; width: 1200px; height: 186px; }
  .site-footer svg { position: absolute; inset: 0; }
  .site-footer .brand { left: 146px; top: 86px; }
  .site-footer .social { left: 384px; top: 97px; }
  .footer-links { left: 615px; top: 58px; font-size: 14.5px; line-height: 33px; color: var(--white); }
  .copyright { left: 925px; top: 85px; font-size: 14.5px; line-height: 27px; color: var(--white); }
</style>
</head>
<body>
  <header class="site-header">
    <div class="abs brand"><span class="brand-mark"></span><span class="brand-name">CoatCraft USA</span></div>
    <nav class="abs nav"><span>HOME</span><span>SERVICES</span><span>PICTURES</span></nav>
    <div class="abs social"><span></span><span></span><span></span></div>
    <a class="abs btn btn-call">CALL</a>
  </header>

  <section class="abs hero">
    <div class="hero-photo" role="img" aria-label="Painters on a red boom lift working on a white commercial building facade"></div>
    <svg class="hero-band" viewBox="0 0 912 200" preserveAspectRatio="none" aria-hidden="true">
      <path d="M0 30 Q120 0 260 22 Q420 44 560 14 Q720 -4 912 40 L912 200 L0 200 Z" fill="#c0001c"/>
    </svg>
    <p class="abs hero-title">Lorem Ipsum is simply dummy text<br>of the printing and typesetting industry.</p>
    <a class="abs btn btn-navy">REQUEST FOR ESTIMATE</a>
  </section>

  <section class="about">
    <div class="photo photo-about" role="img" aria-label="Worker in a hard hat and safety vest painting a wall with a roller"></div>
    <h2 class="abs">About the<br>Coat<span class="accent">Craft</span> USA</h2>
    <p class="abs copy">Lorem Ipsum is simply dummy text of the printing and typesetting industry. Lorem Ipsum has been the industry's standard dummy text ever since the 1500s, when an unknown printer took a galley of type and scrambled it to make a type specimen book. It has survived not only five centuries,</p>
    <a class="abs btn btn-navy">Learn More</a>
  </section>

  <section class="services">
    <h2 class="abs">Take A Services</h2>
    <p class="abs copy">Lorem Ipsum is simply dummy text of the printing and typesetting industry. Lorem Ipsum has been the industry's standard dummy text ever since the 1500s, when an unknown printer took a galley of type and scrambled it to make a type specimen book. It has survived not only five centuries,</p>
    <a class="abs btn btn-red">View More</a>
    <div class="photo photo-services" role="img" aria-label="Apartment building facade being repainted in red and white with a worker on scaffolding"></div>
  </section>

  <section class="gallery">
    <div class="photo photo-gallery" role="img" aria-label="Two painters in white protective suits working on a building wall"></div>
    <h2 class="abs">View Our Gallery</h2>
    <p class="abs copy">Lorem Ipsum is simply dummy text of the printing and typesetting industry. Lorem Ipsum has been the industry's standard dummy text ever since the 1500s, when an unknown printer .</p>
    <a class="abs btn btn-navy">View Gallery</a>
  </section>

  <footer class="abs site-footer">
    <svg viewBox="0 0 1200 186" preserveAspectRatio="none" aria-hidden="true">
      <path d="M0 22 Q150 4 320 16 Q600 30 860 10 Q1040 0 1200 20 L1200 186 L0 186 Z" fill="#4a2326"/>
    </svg>
    <div class="abs brand"><span class="brand-mark"></span><span class="brand-name">CoatCraft USA</span></div>
    <div class="abs social"><span></span><span></span><span></span></div>
    <div class="abs footer-links">Home<br>Services<br>Pictures</div>
    <div class="abs copyright">Copyright © 2023.<br>CoatCraft USA.</div>
  </footer>
</body>
</html>
```